Resume build

I need someone to develop a resume for me. This needs to include a stylized template as well as improving the content of my existing resume.
Updates

All content generated. Just need resume to be formatted and stylized a few different options. With offer a few different head shots to go into it as well. Final versions to be in PDF.

Target Market(s)

this is not for finding a job but is for presenting to clients on who I am and why I'm the qualified candidate to perform their work.

Industry/Entity Type

Marine

Colors
0054AA
0677BA
7BADD7
CADEEF
E8F1F8

Requirements
Must have
• must be in PDF and have a location to add a picture later in the top corner

```html
<!DOCTYPE html>
<html lang="en">
<head>
<meta charset="utf-8">
<title>Rowan Thale – Marine Profile</title>
<link rel="stylesheet" href="https://fonts.googleapis.com/css2?family=Barlow+Condensed:wght@500&family=Montserrat:ital,wght@0,400;0,600;0,700;0,800;1,700&display=swap">
<style>
  :root{
    --navy:#0c2471;
    --ink:#2b3346;
    --muted:#c9d3ea;
    --pill:#dfe7f5;
    --rule:#6c7388;
    --paper:#ffffff;
    --backdrop:#e8edf3;
  }
  *{box-sizing:border-box;margin:0;padding:0}
  html,body{width:1200px;height:800px;overflow:hidden}
  body{background:var(--backdrop);font-family:"Montserrat",sans-serif;color:var(--ink)}
  .page{position:absolute;left:300px;top:12px;width:600px;height:776px;background:var(--paper);display:flex;overflow:hidden;box-shadow:0 2px 10px rgba(0,0,0,.12)}
  .sidebar{flex:none;width:228px;background:var(--navy);color:#fff;padding:28px 14px 14px 18px;display:flex;flex-direction:column}
  .headshot{flex:none;width:160px;height:176px;border:4px solid var(--muted);border-radius:12px;background:linear-gradient(160deg,#5b5e66,#2e3037 60%,#1b2030);margin:0 0 12px 6px}
  .name{font-family:"Barlow Condensed",sans-serif;font-weight:500;font-size:36px;line-height:1;margin-bottom:8px;letter-spacing:.3px}
  .contact{list-style:none;font-size:9.5px;line-height:1.3}
  .contact li{display:flex;align-items:flex-start;gap:8px;margin-bottom:4px}
  .contact svg{flex:none;width:13px;height:13px;margin-top:1px}
  .tagline{margin:8px 0 12px;font-style:italic;font-weight:700;font-size:10.5px;line-height:1.3;text-decoration:underline}
  .side-heading{align-self:flex-start;background:var(--pill);color:var(--navy);font-weight:800;font-size:11px;padding:3px 14px 3px 10px;border-radius:0 12px 12px 0;margin:0 0 7px -4px;text-transform:uppercase}
  .timeline{list-style:none;border-left:1px solid var(--muted);margin-left:4px;padding-left:10px;margin-bottom:12px}
  .timeline li{position:relative;font-size:8.2px;line-height:1.3;color:var(--muted);margin-bottom:5px}
  .timeline li::before{content:"";position:absolute;left:-14px;top:3px;width:5px;height:5px;border:1.5px solid #fff;border-radius:50%;background:var(--navy)}
  .timeline strong{color:#fff;font-weight:700;display:flex;justify-content:space-between}
  .timeline .yr{font-weight:600}
  .certs{margin-bottom:0}
  .certs li{color:#fff;font-size:8.2px;line-height:1.25;margin-bottom:2px}
  .main{flex:1;padding:22px 20px 14px 18px;position:relative}
  .main::after{content:"";position:absolute;left:0;right:0;bottom:0;height:5px;background:var(--navy)}
  .main-heading{display:flex;align-items:center;gap:8px;font-weight:800;font-size:14px;color:var(--ink);margin-bottom:8px}
  .main-heading::after{content:"";flex:1;height:1px;background:var(--rule)}
  .role{margin-bottom:7px}
  .role-head{display:flex;justify-content:space-between;color:var(--navy);font-weight:700;font-size:8.6px;line-height:1.28}
  .role-date{font-style:italic;white-space:nowrap}
  .role ul{list-style:none;margin-top:2px}
  .role li{position:relative;padding-left:12px;font-size:8px;line-height:1.3;margin-bottom:1px}
  .role li::before{content:"";position:absolute;left:1px;top:3px;width:4px;height:4px;border:1.5px solid var(--navy);border-radius:50%}
</style>
</head>
<body>
<main class="page">
  <aside class="sidebar">
    <div class="headshot" role="img" aria-label="Headshot of Rowan Thale in a dark blazer"></div>
    <h1 class="name">Rowan Thale</h1>
    <ul class="contact">
      <li><svg viewBox="0 0 14 14"><circle cx="7" cy="7" r="7" fill="#fff"/><path d="M7 3.2a2.4 2.4 0 0 0-2.4 2.4C4.6 7.4 7 10.6 7 10.6s2.4-3.2 2.4-5A2.4 2.4 0 0 0 7 3.2z" fill="#0c2471"/><circle cx="7" cy="5.6" r=".9" fill="#fff"/></svg><span>2240 Harbourview Lane<br>Victoria, BC Canada V8X 1K4</span></li>
      <li><svg viewBox="0 0 14 14"><circle cx="7" cy="7" r="7" fill="#fff"/><path d="M5 3.6l1.2 1.8-.8.8c.4.9 1.1 1.6 2 2l.8-.8 1.8 1.2-.6 1.2c-2.6-.2-4.6-2.2-4.8-4.8z" fill="#0c2471"/></svg><span>1 (555) 014 2290</span></li>
      <li><svg viewBox="0 0 14 14"><circle cx="7" cy="7" r="7" fill="#fff"/><rect x="3.6" y="4.6" width="6.8" height="4.8" rx=".6" fill="#0c2471"/><path d="M3.9 5l3.1 2.4L10.1 5" stroke="#fff" stroke-width=".8" fill="none"/></svg><span>rowan@tidelinemarine.com</span></li>
    </ul>
    <p class="tagline">A proven expert in marine project<br>management and operation</p>

    <h2 class="side-heading">Education</h2>
    <ul class="timeline">
      <li><strong>Nautical Sciences Degree <span class="yr">2004 - 2008</span></strong>Pacific Institute of Technology<br>North Vancouver, British Columbia</li>
      <li><strong>Associate of Arts Degree <span class="yr">2001 - 2003</span></strong>Harbourside College<br>Vancouver, British Columbia</li>
    </ul>

    <h2 class="side-heading">Certifications &amp; Skills</h2>
    <ul class="timeline certs">
      <li>Master Mariner</li>
      <li>Certificate in the Fundamentals of Liquefied Natural Gas, Anchorline Maritime Academy</li>
      <li>Incident Command Training 100</li>
      <li>Bridge Resource Management Certificate</li>
      <li>Ship Security Officer</li>
      <li>Basic Tanker Safety Certificate</li>
      <li>Basic Safety Training</li>
      <li>Marine Advanced Firefighting</li>
      <li>Marine Emergency Duties Senior Officer</li>
      <li>Proficiency in Survival Craft Certificate</li>
      <li>General Operators GMDSS Certificate</li>
      <li>Fast Rescue Craft Certificate</li>
      <li>Marine Advanced First Aid</li>
    </ul>
  </aside>

  <section class="main">
    <h2 class="main-heading">EXPERIENCE</h2>

    <article class="role">
      <div class="role-head"><span>Tideline Marine Ltd., Co-Founder/Managing Director<br>Victoria, British Columbia</span><span class="role-date">2015 - Present</span></div>
      <ul>
        <li>Manage complex multi-million-dollar marine projects from inception through to execution</li>
        <li>Guide clients through regulatory processes with marine government regulators</li>
        <li>Represent owners in new vessel construction and refit projects globally</li>
        <li>Supply and operate passenger vessels for custom client projects</li>
        <li>Design &amp; implementation of National Transport Authority approved Safety Management Systems</li>
        <li>Advise clients through marine start-ups and business planning</li>
        <li>Supply personnel to various marine operators globally as needed</li>
      </ul>
    </article>

    <article class="role">
      <div class="role-head"><span>Coastline Ferries, Senior Manager, Nautical Standards<br>Victoria, British Columbia</span><span class="role-date">2019 - 2021</span></div>
      <ul>
        <li>Manages the procurement, implementation and life-cycle management of fleet-wide deck department safety critical assets &amp; navigational equipment for fleet of 38 vessels</li>
        <li>Chairs the Nautical Standards Committee and Vessel Electronics Program that oversees the selection and implementation of fleet equipment</li>
        <li>Works with the Fleet Technical and Vessel Replacement divisions in the selection process for new major equipment</li>
        <li>Advises on design and equipment profiles for new vessel construction</li>
        <li>Develops new initiatives to ensure vessel performance and readiness</li>
      </ul>
    </article>

    <article class="role">
      <div class="role-head"><span>Coastline Ferries, Senior Captain<br>South Coast, British Columbia</span><span class="role-date">2017 - 2019</span></div>
      <ul>
        <li>Captain and vessel manager</li>
        <li>Responsible for overall operation of the vessel including navigation, budgeting, labour, safety management, regulatory compliance, deck maintenance &amp; training</li>
        <li>Responsible for up to 30 crew/staff</li>
      </ul>
    </article>

    <article class="role">
      <div class="role-head"><span>Pacific Marine Search &amp; Rescue, Safety Manager<br>Victoria, British Columbia</span><span class="role-date">2013 - 2017</span></div>
      <ul>
        <li>Implemented a provincial wide safety management program for marine search and rescue</li>
        <li>Managed a five-member safety team representing various regions across the province</li>
        <li>Drafted and issued new policies including Standard Operating Procedures, Annual Vessel Inspections, Vessel Familiarizations &amp; Planned Vessel Maintenance</li>
      </ul>
    </article>

    <article class="role">
      <div class="role-head"><span>Port of Westhaven, Operations Coordinator<br>Vancouver, British Columbia</span><span class="role-date">2012 - 2016</span></div>
      <ul>
        <li>Oversaw the safe and efficient operations of marine activity within Port of Westhaven's jurisdiction acting as the Harbour Masters representative</li>
        <li>Responded to marine, land and security incidents, ensuring initial actions were taken by relevant parties</li>
        <li>Acted as the initial and primary means of communication between the Port and external stakeholders, regulatory agencies and the public</li>
      </ul>
    </article>

    <article class="role">
      <div class="role-head"><span>Meridian Cruises, Chief Officer<br>Folkestone, United Kingdom</span><span class="role-date">2008 - 2011</span></div>
      <ul>
        <li>Managed a 20-man deck department including 2 watch-keeping officers, 2 bosons and 16 able-bodied and ordinary seamen</li>
        <li>Held daily 4-8 watch in a single watch-keeping system conducting the majority of arrivals and departures in ports all over the world</li>
      </ul>
    </article>

    <article class="role">
      <div class="role-head"><span>Various Vessels Operating Globally<br>Junior Navigational Officer</span><span class="role-date">2004 - 2008</span></div>
      <ul>
        <li>Responsibilities included: holding regular navigational watch, mooring stations, all official logbooks, chart corrections, lifeboat maintenance, meteorological observations and fire-fighting equipment maintenance</li>
      </ul>
    </article>
  </section>
</main>
</body>
</html>
```